Soho based IT support firm flyer.

We need a flyer to boost our business. We're a tech support firm based in Soho, London and provide helpdesk and call out support to SMEs in and around London.
They'll be two flyers with the same design. One is location specific and has the copy:
-
1 Month Free IT Support!
Based in Soho, we provide expert tech support for both Zelks and PCs.
We have monthly as well as pay-as-you-go plans to fit your business.
Call us now and we'll show you how we can save you up to 50% on your IT spend.
-None location based is-
1 Month Free IT Support!
We provide expert, professional tech support for both Zelks and PCs.
• Dedicated full time helpdesk
• Same day onsite visits
• Proactive support with monitoring
• 98% satisfaction score*
*taken from satisfaction survey sent out on closure of every case for Oct 2011 to Oct 2012
-
The location one needs to include a map with our location marked as postcode Q9X 4TT.
I'm fine with royalty photos being used within a reasonable price. Please use PicturVault.
Our site shows our brand best. Please keep as close to this as possible.
http://brivo-desk.example
Thanks for looking.

```html
<!DOCTYPE html>
<html lang="en">
<head>
<meta charset="utf-8">
<title>Brivo Desk – Soho IT Support Flyer</title>
<link rel="stylesheet" href="https://fonts.googleapis.com/css2?family=Comic+Neue:wght@400;700&family=Chewy&display=swap">
<style>
  :root {
    --stage: #2b2b2b;
    --paper: #f8f9ef;
    --ink: #3a3a36;
    --lime: #8fa320;
    --band: #c7cb4c;
    --band-light: #d9dc72;
    --orange: #f6a531;
    --orange-soft: #fbd08c;
    --olive: #a9b232;
    --olive-deep: #7f8a1c;
    --white: #ffffff;
  }
  * { margin: 0; padding: 0; box-sizing: border-box; }
  html, body {
    width: 1072px; height: 1200px; overflow: hidden;
    background: var(--stage);
  }
  .flyer {
    position: absolute; left: 143px; top: 60px;
    width: 786px; height: 1080px;
    background: var(--paper);
    overflow: hidden;
    font-family: "Comic Neue", "Comic Sans MS", cursive;
    color: var(--ink);
  }
  .swoosh-layer { position: absolute; inset: 0; }
  .brand {
    position: absolute; top: 40px; left: 0; right: 0;
    display: flex; justify-content: center; align-items: center; gap: 16px;
    font-weight: 700; font-size: 62px; color: var(--lime);
  }
  .brand-dot { width: 30px; height: 30px; border-radius: 50%; background: var(--lime); }
  .intro, .plans {
    position: absolute; left: 0; width: 560px;
    text-align: center; font-size: 40px; line-height: 58px;
  }
  .intro { top: 195px; }
  .intro .platforms { font-size: 48px; font-weight: 700; line-height: 70px; }
  .intro .platforms .hl { color: var(--lime); }
  .offer-band {
    position: absolute; left: 0; right: 0; top: 490px; height: 110px;
    background: linear-gradient(var(--band) 0 65%, var(--band-light) 65% 100%);
  }
  .offer-band h1 {
    position: absolute; left: 0; right: 0; top: 8px;
    text-align: center;
    font-family: "Chewy", "Comic Neue", cursive; font-weight: 700;
    font-size: 50px; line-height: 56px; letter-spacing: 1px; color: var(--white);
    text-shadow: 2px 2px 0 #5a5a4a, -1px -1px 0 #5a5a4a, 1px -1px 0 #5a5a4a, -1px 1px 0 #5a5a4a;
  }
  .plans { top: 648px; }
  .mascot {
    position: absolute; left: 600px; top: 566px; width: 150px; height: 200px;
    border-radius: 40px 40px 20px 20px;
    background: linear-gradient(160deg, #f1d9b8, #3f6f9a);
  }
  .tech-skyline {
    position: absolute; left: 630px; top: 770px; width: 156px; height: 130px;
    background: linear-gradient(180deg, var(--olive) 0%, var(--olive-deep) 100%);
    border-radius: 50px 0 0 0;
  }
  .contact {
    position: absolute; left: 0; right: 0; top: 938px;
    text-align: center; color: var(--white);
    font-family: "Chewy", "Comic Neue", cursive; font-weight: 700;
  }
  .phone {
    font-size: 46px; line-height: 52px; color: var(--orange); letter-spacing: 2px;
    text-shadow: 2px 2px 0 #5a4a1a, -1px -1px 0 #5a4a1a;
    display: flex; justify-content: center; align-items: center; gap: 12px;
  }
  .phone svg { width: 32px; height: 32px; }
  .rule { width: 560px; margin: 4px auto 6px; border-top: 2px dashed rgba(255,255,255,0.85); }
  .call-to-action { font-size: 28px; line-height: 36px; text-shadow: 1px 1px 0 #55581a; }
  .call-to-action .hl { color: var(--orange); }
</style>
</head>
<body>
  <main class="flyer">
    <svg class="swoosh-layer" viewBox="0 0 786 1080" preserveAspectRatio="none" aria-hidden="true">
      <defs>
        <linearGradient id="base-fill" x1="0" y1="0" x2="0" y2="1">
          <stop offset="0" stop-color="#bcc23e"/>
          <stop offset="1" stop-color="#8d9a1f"/>
        </linearGradient>
      </defs>
      <path d="M0 158 C 220 130, 520 170, 786 300 L786 330 C 520 200, 260 160, 0 178 Z" fill="var(--orange)"/>
      <path d="M0 178 C 260 160, 520 200, 786 330 L786 345 C 520 215, 260 175, 0 190 Z" fill="var(--orange-soft)"/>
      <path d="M0 770 C 200 870, 480 900, 786 898 L786 914 C 480 916, 200 892, 0 792 Z" fill="var(--orange)"/>
      <path d="M0 792 C 200 892, 480 916, 786 914 L786 1080 L0 1080 Z" fill="url(#base-fill)"/>
    </svg>

    <div class="brand"><span class="brand-dot"></span>Brivo Desk</div>

    <p class="intro">Based in Soho,<br>we provide expert<br>tech support for both<br>
      <span class="platforms"><span class="hl">Zelks</span> and <span class="hl">PCs</span>.</span></p>

    <section class="offer-band"><h1>1 Month Free IT Support!</h1></section>

    <p class="plans">We have monthly as well as<br>pay-as-you-go plans to fit<br>your business.</p>

    <div class="mascot" role="img" aria-label="Cartoon technician character hanging below the offer band"></div>
    <div class="tech-skyline" role="img" aria-label="Green silhouette of office equipment and desk lamp"></div>

    <section class="contact">
      <div class="phone">
        <svg viewBox="0 0 24 24" aria-hidden="true"><path fill="currentColor" d="M6.6 10.8a15.2 15.2 0 0 0 6.6 6.6l2.2-2.2a1 1 0 0 1 1-.25 11.4 11.4 0 0 0 3.6.57 1 1 0 0 1 1 1V20a1 1 0 0 1-1 1A17 17 0 0 1 3 4a1 1 0 0 1 1-1h3.5a1 1 0 0 1 1 1c0 1.25.2 2.45.57 3.6a1 1 0 0 1-.25 1z"/></svg>
        1600-555-014
      </div>
      <div class="rule"></div>
      <p class="call-to-action">Call us now and we'll show you how we<br>can save you up to <span class="hl">50%</span> on your IT spend.</p>
    </section>
  </main>
</body>
</html>
```